Lighting bulbs packaging design

My company is a lighting products manufacturer. Our trademark is "quarnix". I need packaging design for 2 series of lighting bulbs.
1. HID bulbs.
2. Vintage filament bulbs. (need lighting bulb label on one side)

Industry/Entity Type

It Company

Colors

Designer to choose colors to be used in the design.

```html
<!DOCTYPE html>
<html lang="en">
<head>
<meta charset="utf-8">
<title>Quarnix Vintage Filament Bulb – Box Dieline</title>
<link href="https://fonts.googleapis.com/css2?family=Arimo:wght@400;700&display=swap" rel="stylesheet">
<style>
  :root {
    --paper: #ffffff;
    --yellow: #f6c400;
    --yellow-deep: #f0b400;
    --glow: #fffbe8;
    --ink: #3b3b3b;
    --ink-soft: #5c5c5c;
    --rule: #6b6b6b;
    --fold: #f2f2f2;
    --frame: #d6d6d6;
  }
  * { box-sizing: border-box; margin: 0; padding: 0; }
  html, body { width: 1200px; height: 981px; overflow: hidden; background: var(--paper); }
  body { font-family: "Arimo", Arial, sans-serif; color: var(--ink); }
  .canvas { position: relative; width: 1200px; height: 981px; }
  .page-frame { position: absolute; left: 105px; top: -1px; width: 1100px; height: 981px; border: 1px solid var(--frame); }
  .dieline { position: absolute; left: 0; top: 0; }

  .abs { position: absolute; }
  .art { position: absolute; border-radius: 50%; }
  .art-mascot { background: radial-gradient(circle at 45% 55%, #ffe14a 0 45%, #3a3a3a 46% 60%, transparent 61%); }
  .art-bulb { border-radius: 48% 48% 30% 30%; background: linear-gradient(180deg, rgba(255,255,255,.95) 0%, rgba(240,240,240,.9) 62%, #7a7a7a 63%, #4a4a4a 100%); }

  .wordmark { position: absolute; font-weight: 700; font-size: 27px; letter-spacing: 2px; color: var(--ink); text-transform: uppercase; text-align: center; width: 200px; }

  .rating-badge { position: absolute; width: 58px; font-weight: 700; font-size: 19px; line-height: 1; text-align: center; }
  .rating-badge .watt { background: var(--yellow); border: 2px solid var(--ink); border-bottom: 0; border-radius: 6px 6px 0 0; padding: 2px 0; color: var(--ink); }
  .rating-badge .volt { background: var(--paper); border: 2px solid var(--ink); padding: 2px 0; color: var(--ink); }

  .product-name { position: absolute; width: 110px; text-align: center; font-weight: 700; font-size: 14.5px; line-height: 17px; color: var(--ink); }

  .lid-top { position: absolute; left: 233px; top: 33px; width: 222px; height: 267px; transform: rotate(180deg); }

  .lighting-facts { position: absolute; left: 460px; top: 385px; width: 208px; color: var(--ink-soft); font-size: 11px; }
  .lighting-facts h2 { font-size: 19px; font-weight: 700; color: var(--ink-soft); }
  .lighting-facts h2 small { font-size: 10px; font-weight: 400; }
  .lighting-facts .bar { height: 8px; background: var(--rule); margin: 2px 0 3px; }
  .lighting-facts .row { display: flex; justify-content: space-between; font-weight: 700; }
  .lighting-facts .note { font-weight: 400; font-size: 9.5px; padding-left: 8px; line-height: 12px; }
  .lighting-facts .sep { border-top: 1px solid var(--rule); margin: 4px 0 3px; }
  .lighting-facts .scale { position: relative; height: 30px; font-size: 10px; font-weight: 400; }
  .lighting-facts .scale .line { position: absolute; left: 36px; right: 28px; top: 14px; height: 3px; background: var(--rule); }
  .lighting-facts .scale .tri { position: absolute; left: 38px; top: 12px; width: 0; height: 0; border-left: 5px solid transparent; border-right: 5px solid transparent; border-bottom: 8px solid var(--rule); }

  .lid-bottom-text { position: absolute; transform: rotate(180deg); font-size: 10.5px; color: var(--ink-soft); letter-spacing: .3px; }
  .care-icons { position: absolute; left: 730px; top: 877px; width: 112px; height: 20px; border-radius: 10px; background: linear-gradient(90deg, #5a5a5a, #7a7a7a); opacity: .8; }

  .specs { position: absolute; left: 912px; top: 361px; font-size: 12.5px; line-height: 15px; color: var(--ink-soft); }
  .specs h3 { font-size: 12.5px; font-weight: 700; }
  .specs ul { list-style: none; margin-top: 15px; }
  .info-box { position: absolute; left: 926px; top: 501px; width: 161px; height: 81px; background: var(--paper); border: 1px solid #cfcfcf; font-size: 9px; padding: 1px 3px; color: var(--ink-soft); }
</style>
</head>
<body>
<div class="canvas">
  <div class="page-frame"></div>

  <svg class="dieline" width="1200" height="981" viewBox="0 0 1200 981" aria-hidden="true">
    <defs>
      <radialGradient id="panel-glow" cx="50%" cy="50%" r="70%">
        <stop offset="0" stop-color="var(--glow)" style="stop-color:#fffdf0"/>
        <stop offset=".35" stop-color="#fde98a"/>
        <stop offset=".75" stop-color="#f6c400"/>
        <stop offset="1" stop-color="#f0b400"/>
      </radialGradient>
      <linearGradient id="flap-glow" x1="0" y1="0" x2="1" y2="1">
        <stop offset="0" stop-color="#f6c400"/>
        <stop offset=".5" stop-color="#fbe07a"/>
        <stop offset="1" stop-color="#f4be00"/>
      </linearGradient>
    </defs>
    <g stroke="#f4f4f4" stroke-width="1">
      <!-- glue flap -->
      <polygon points="175,312 233,300 233,686 175,673" fill="url(#flap-glow)"/>
      <!-- front panel + lid + tuck -->
      <polygon points="238,33 450,33 455,80 455,686 233,686 233,80" fill="url(#flap-glow)"/>
      <rect x="233" y="300" width="222" height="386" fill="url(#panel-glow)"/>
      <!-- facts panel + flaps -->
      <polygon points="455,193 640,193 675,300 455,300" fill="url(#flap-glow)"/>
      <rect x="455" y="300" width="220" height="386" fill="url(#panel-glow)"/>
      <polygon points="455,686 675,686 675,795 490,795" fill="url(#flap-glow)"/>
      <!-- second front panel + bottom lid + tuck -->
      <rect x="675" y="300" width="222" height="386" fill="url(#panel-glow)"/>
      <polygon points="675,686 897,686 897,905 887,955 685,955 675,905" fill="url(#flap-glow)"/>
      <!-- specs panel + flaps -->
      <polygon points="897,300 930,193 1117,193 1117,300" fill="url(#flap-glow)"/>
      <rect x="897" y="300" width="220" height="386" fill="url(#panel-glow)"/>
      <polygon points="897,686 1117,686 1087,795 897,795" fill="url(#flap-glow)"/>
      <!-- fold lines -->
      <line x1="233" y1="80" x2="455" y2="80"/>
      <line x1="675" y1="905" x2="897" y2="905"/>
    </g>
  </svg>

  <!-- top lid (upside down) -->
  <div class="lid-top">
    <div class="art art-mascot" role="img" aria-label="Bee mascot illustration" style="left:80px;top:-15px;width:90px;height:95px"></div>
    <div class="wordmark" style="left:11px;top:105px">quarnix</div>
    <div class="rating-badge" style="left:0;top:172px">
      <div class="watt">60W</div><div class="volt">120V</div>
    </div>
    <div class="product-name" style="left:70px;top:190px">VINTAGE<br>FILAMENT<br>BULB</div>
  </div>

  <!-- front panel -->
  <div class="art art-mascot" role="img" aria-label="Bee mascot illustration" style="left:285px;top:303px;width:90px;height:92px"></div>
  <div class="wordmark" style="left:240px;top:394px">quarnix</div>
  <div class="art art-bulb" role="img" aria-label="Quad loop vintage filament bulb illustration" style="left:278px;top:440px;width:130px;height:238px"></div>
  <div class="rating-badge" style="left:233px;top:560px"><div class="watt">60W</div><div class="volt">120V</div></div>
  <div class="product-name" style="left:220px;top:609px">VINTAGE<br>FILAMENT<br>BULB</div>

  <!-- lighting facts panel -->
  <section class="lighting-facts">
    <h2>Lighting Facts <small>Per Bulb</small></h2>
    <div class="bar"></div>
    <div class="row"><span>Brightness</span><span>XXX lumens</span></div>
    <div class="sep"></div>
    <div class="row"><span>Estimated Yearly Energy Cost</span><span>$X.XX</span></div>
    <div class="note">Based on 3 hrs/day, 11¢/kWh<br>Cost depends on rates and use</div>
    <div class="sep"></div>
    <div class="row"><span>Life</span></div>
    <div class="row"><span class="note">Based on 3 hrs/day</span><span>X.X years</span></div>
    <div class="sep"></div>
    <div class="row"><span>Light Appearance</span></div>
    <div class="scale">
      <span class="abs" style="left:20px;top:0">Warm</span>
      <span class="abs" style="right:22px;top:0">Cool</span>
      <div class="line"></div><div class="tri"></div>
      <span class="abs" style="left:28px;top:21px">XXXX K</span>
    </div>
    <div class="sep"></div>
    <div class="row"><span>Energy Used</span><span>XX watts</span></div>
  </section>

  <!-- second front panel -->
  <div class="art art-mascot" role="img" aria-label="Bee mascot illustration" style="left:727px;top:303px;width:90px;height:92px"></div>
  <div class="wordmark" style="left:682px;top:394px">quarnix</div>
  <div class="art art-bulb" role="img" aria-label="Quad loop vintage filament bulb illustration" style="left:720px;top:440px;width:130px;height:238px"></div>
  <div class="rating-badge" style="left:675px;top:560px"><div class="watt">60W</div><div class="volt">120V</div></div>
  <div class="product-name" style="left:662px;top:609px">VINTAGE<br>FILAMENT<br>BULB</div>

  <!-- bottom lid -->
  <div class="lid-bottom-text" style="left:743px;top:725px">MADE IN CHINA</div>
  <div class="lid-bottom-text" style="left:800px;top:794px">MANUFACTURED</div>
  <div class="care-icons" role="img" aria-label="Handling and recycling symbols"></div>

  <!-- specifications panel -->
  <section class="specs">
    <h3>SPECIFICATIONS</h3>
    <div>Quarnix Quad Loop Filament Bulb</div>
    <ul>
      <li>Wattage: 60 Watt</li>
      <li>Voltage: 120</li>
      <li>Bulb Color: Clear</li>
      <li>Bulb Shape: A19</li>
      <li>Base Type: Medium (E26)</li>
      <li>Life span: 2500 hrs</li>
    </ul>
  </section>
  <div class="info-box">Company information</div>
</div>
</body>
</html>
```